Glanvero foot health or foot health glanvero

Treatments in comfort of your own home
Delia Marsh cert KTRVb Pod, LQNDoct
Treatments will be listed on the leaflet I will attach
I am a Foot Health practitioner,
I want to mention I do home visits throughout Pembrokeshire & Ceredigion.
Tel. 07604519283
I have 2 logs to forward to you they are the associations I belong to .
One of which is also a certification mark. It is important that the same colour is used for this mark. They are not the main focus, they are just recognised mark. To be at the top or bottom of the page.
There is a local business called Tregarrow foot clinic, so my business has to be glanvero foot health, or foot health glanvero
soon I will also need a web page and cards designed, so please keep this in mind when designing the Artwork. I will also need an email on the leaflet but I will wait and see what the design is first before I confirm it as I have several.
I hope this is enough info for you.
Many thanks,
Delia Marsh

Target Market(s)

Mostly the elderly, some middle age women, but it is a service for all ages. The elderly are my main clients.

Industry/Entity Type

Health

Font styles to use
Serif
Sans Serif

Colors

Designer to choose colors to be used in the design.

Requirements
Must have
• Covering Pembrokeshire & Ceredigion.
Treatments include:- as listed on example leaflet I sent
Phone number a size that's easily readable.
I am open to colours. I love bright colours, but also like the more conservative colours as long as it looks professional. I'm wanting it to look more up market.
Nice to have
• Logo for Guildhall and KTE logo obviously smaller, but also recognisable and either at the top of page or bottom. These are not to be main focal point.

```html
<!DOCTYPE html>
<html lang="en">
<head>
<meta charset="utf-8">
<title>Glanvero Foot Health – Leaflet</title>
<link href="https://fonts.googleapis.com/css2?family=Noto+Sans:wght@400;700&display=swap" rel="stylesheet">
<style>
  :root {
    --ink: #1e1e1e;
    --night: #232323;
    --sun: #ffd800;
    --sun-deep: #f2b400;
    --cream: #fff3c4;
    --paper: #ffffff;
    --panel: rgba(40, 32, 10, 0.78);
  }
  * { box-sizing: border-box; margin: 0; padding: 0; }
  html, body { width: 847px; height: 1200px; overflow: hidden; background: var(--paper); }
  body { font-family: "Noto Sans", Verdana, sans-serif; }

  .leaflet { position: relative; width: 847px; height: 1200px; overflow: hidden; background: var(--night); }

  .masthead { position: absolute; left: 0; top: 0; width: 847px; height: 206px; background: var(--night); }
  .brand-name {
    position: absolute; left: 76px; top: 36px;
    color: var(--sun); font-weight: 700; font-size: 54px; line-height: 70px;
  }
  .brand-mark {
    position: absolute; right: 82px; top: 30px; width: 96px; height: 146px;
  }

  .divider { position: absolute; left: 0; width: 847px; height: 6px; background: var(--paper); }
  .divider--top { top: 206px; }
  .divider--bottom { top: 982px; }

  .hero {
    position: absolute; left: 0; top: 212px; width: 847px; height: 770px;
    background:
      radial-gradient(ellipse at 25% 55%, #ffe866 0%, rgba(255,232,102,0) 45%),
      radial-gradient(ellipse at 80% 30%, #ffd200 0%, rgba(255,210,0,0) 55%),
      linear-gradient(160deg, var(--sun) 0%, var(--sun-deep) 100%);
  }

  .tagline {
    position: absolute; left: 76px; top: 236px; width: 700px;
    color: var(--ink); font-weight: 700; font-size: 30px; line-height: 38px;
  }

  .treatments {
    position: absolute; left: 75px; top: 349px; width: 698px; height: 280px;
    background: var(--panel); border-radius: 14px;
    text-align: center; padding-top: 22px;
  }
  .treatments__title { color: var(--paper); font-weight: 700; font-size: 29px; line-height: 40px; }
  .treatments__list { list-style: none; color: var(--cream); font-size: 28px; line-height: 50px; }

  .contact { position: absolute; left: 76px; top: 652px; width: 380px; color: var(--ink); }
  .contact__lead { font-weight: 700; font-size: 28px; line-height: 33px; }
  .contact__name { font-weight: 700; font-size: 28px; line-height: 34px; margin-top: 4px; }
  .contact__certs { font-size: 22px; line-height: 26px; }

  .memberships {
    position: absolute; left: 75px; top: 867px; width: 298px; height: 77px;
    background: rgba(255,255,255,0.82); border-radius: 10px;
  }
  .memberships__badge { position: absolute; top: 12px; }
  .memberships__badge--register { left: 14px; width: 150px; height: 52px; background: #6b3fa0; border-radius: 8px; }
  .memberships__badge--association { left: 196px; width: 56px; height: 56px; top: 10px; background: #2f8f3a; border-radius: 50%; }

  .visit-photo {
    position: absolute; left: 460px; top: 672px; width: 313px; height: 272px;
    border: 6px solid var(--paper); border-radius: 16px;
    background: linear-gradient(135deg, #f3eef0 0%, #e8c9c2 45%, #2c3340 100%);
  }

  .footer { position: absolute; left: 0; top: 988px; width: 847px; height: 212px; background: var(--night); }
  .footer__mark {
    position: absolute; left: -20px; top: 40px; width: 130px; height: 190px;
    background: rgba(255,255,255,0.08); border-radius: 60px;
  }
  .footer__line {
    position: absolute; left: 0; width: 847px; text-align: center;
    color: var(--paper); font-size: 38px; line-height: 46px;
  }
  .footer__line--phone { top: 16px; }
  .footer__line--email { top: 62px; }
  .footer__area {
    position: absolute; left: 0; top: 130px; width: 847px; text-align: center;
    color: var(--sun); font-weight: 700; font-size: 32px; line-height: 40px;
  }
</style>
</head>
<body>
<main class="leaflet">
  <header class="masthead">
    <h1 class="brand-name">Glanvero<br>Foot Health</h1>
    <svg class="brand-mark" role="img" aria-label="Footprint symbol" viewBox="0 0 96 146">
      <ellipse cx="46" cy="88" rx="30" ry="54" fill="var(--sun)"/>
    </svg>
  </header>
  <div class="divider divider--top"></div>

  <section class="hero" role="img" aria-label="Close-up photograph of bare feet in warm yellow light"></section>

  <p class="tagline">All treatments carried out in the comfort of your own home</p>

  <section class="treatments">
    <h2 class="treatments__title">TREATMENTS INCLUDE</h2>
    <ul class="treatments__list">
      <li>Diabetic Foot Care • Ingrowing Toenails</li>
      <li>Corn And Callous Treatment</li>
      <li>Toenail Clipping • Fungal Infections Treated</li>
      <li>Cracked Heals</li>
    </ul>
  </section>

  <section class="contact">
    <p class="contact__lead">For more information or to book an appointment contact:</p>
    <p class="contact__name">Delia Marsh</p>
    <p class="contact__certs">cert KTRVb Pod, LQNDoct</p>
  </section>

  <div class="memberships">
    <span class="memberships__badge memberships__badge--register"></span>
    <span class="memberships__badge memberships__badge--association"></span>
  </div>

  <div class="visit-photo" role="img" aria-label="Photograph of a foot health practitioner treating a client's foot at home"></div>

  <div class="divider divider--bottom"></div>
  <footer class="footer">
    <div class="footer__mark" role="img" aria-label="Faint footprint decoration"></div>
    <p class="footer__line footer__line--phone">T 07604 519283</p>
    <p class="footer__line footer__line--email">E name@address.co.uk</p>
    <p class="footer__area">Covering Pembrokeshire &amp; Ceredigion</p>
  </footer>
</main>
</body>
</html>
```